Business card design for modern law firm

We need new business cards. Information about our law firm can be found at www.qrtl-recht.de. The business cards should include the information that we have offices in Berlin and Stuttgart. They should be customizable for all attorneys who are partially located in Berlin and partially in Stuttgart. Example of the information:
Jonas Ackermann
lawyer
Specialist lawyer for copyright and media law
Lindenweg 17, 70374 Stuttgart
ackermann@qrtl-recht.de
+49 711 483 15 260
www.qrtl-recht.de
It is important for us that we can edit the cards independently, i.e. exchange names and contact details.
In addition, a QR code for a VCard should be placed on the card.
The design of the old maps is attached; the new design should clearly distinguish itself from them. They should be more modern. The design is ideally based on the design of the website www.qrtl-recht.de.
Industry/Entity Type
Rechtsanwalt
Contact Information for Business Card
Siehe projektbeschreibung

```html
<!DOCTYPE html>
<html lang="de">
<head>
<meta charset="utf-8">
<title>QRTL Rechtsanwälte – Visitenkarten</title>
<link href="https://fonts.googleapis.com/css2?family=Open+Sans:wght@400;600;700&display=swap" rel="stylesheet">
<style>
  :root {
    --lime: #a6ce39;
    --lime-soft: #b9d964;
    --black: #000000;
    --white: #ffffff;
    --ink: #6b6b6b;
    --ink-dark: #5a5a5a;
    --shadow: #3a3838;
  }
  * { margin: 0; padding: 0; box-sizing: border-box; }
  html, body { width: 876px; height: 1200px; overflow: hidden; background: var(--white); }
  body { font-family: "Open Sans", Arial, sans-serif; }
  .sheet { position: relative; width: 876px; height: 1200px; background: var(--black); margin-top: 8px; }
  .abs { position: absolute; }

  .brand { font-weight: 600; color: var(--lime); white-space: nowrap; letter-spacing: 1px; }
  .brand--header { left: 56px; top: 44px; font-size: 34px; line-height: 40px; }
  .brand--header .square { display: inline-block; width: 12px; height: 12px; background: var(--lime); margin-right: 12px; vertical-align: middle; }

  .header-address { left: 673px; top: 40px; display: flex; gap: 8px; color: var(--white); font-size: 14px; line-height: 14px; letter-spacing: .6px; }

  .card { position: absolute; width: 557px; height: 334px; }
  .card--front { left: 203px; top: 267px; background: var(--white); box-shadow: 8px 8px 0 var(--shadow); }
  .card-under { position: absolute; left: 195px; top: 275px; width: 557px; height: 334px; background: #f2f2f2; }
  .card--back { left: 199px; top: 642px; background: var(--lime); box-shadow: 14px 14px 16px rgba(60,56,56,.75); }

  .card-brand { left: 0; right: 0; top: 68px; text-align: center; font-size: 26px; }
  .person { left: 0; right: 0; text-align: center; color: var(--ink); }
  .person__name { top: 138px; font-size: 15px; font-weight: 700; letter-spacing: 1.2px; }
  .person__role { top: 156px; font-size: 16px; letter-spacing: .6px; }
  .person__field { top: 179px; font-size: 11.5px; letter-spacing: .5px; }
  .divider { left: 0; right: 0; top: 206px; height: 1px; background: var(--lime); }
  .divider__diamond { left: 274px; top: 202px; width: 8px; height: 8px; background: var(--lime); transform: rotate(45deg); }

  .contact { color: var(--ink); font-size: 11px; display: flex; align-items: center; gap: 6px; white-space: nowrap; }
  .contact svg { flex: none; }
  .contact--phone { left: 173px; top: 231px; }
  .contact--web { left: 334px; top: 229px; }
  .contact--mail { left: 220px; top: 250px; }
  .contact-pin { left: 271px; top: 272px; }
  .contact--address { left: 0; right: 0; top: 289px; justify-content: center; }

  .skyline-brand { left: 36px; top: 214px; color: var(--white); font-weight: 600; font-size: 52px; line-height: 56px; letter-spacing: 2px; }
  .tower-art { left: 220px; top: 126px; width: 40px; height: 131px; background: var(--lime-soft); }
  .ground-line { left: 0; right: 0; top: 259px; height: 4px; background: var(--white); }
  .office { left: 296px; top: 140px; color: var(--white); }
  .office__city { font-size: 22px; font-weight: 700; letter-spacing: 2px; line-height: 28px; }
  .office__line { font-size: 17px; letter-spacing: 1.2px; line-height: 21px; }
  .office__city + .office__line { margin-top: 6px; }

  .footer-band { left: 0; right: 0; top: 1117px; height: 83px; background: var(--lime); }
  .brand--footer { left: 660px; top: 1060px; font-size: 44px; line-height: 52px; }
  .tower-art--footer { left: 805px; top: 1017px; width: 40px; height: 100px; background: #3f4d16; }
</style>
</head>
<body>
<main class="sheet">
  <header>
    <div class="abs brand brand--header"><span class="square"></span>QRTL Rechtsanwälte</div>
    <div class="abs header-address">
      <svg width="17" height="23" viewBox="0 0 17 23" aria-hidden="true"><path d="M8.5 0C3.8 0 0 3.7 0 8.3 0 14 8.5 23 8.5 23S17 14 17 8.3C17 3.7 13.2 0 8.5 0z" fill="#fff"/><circle cx="8.5" cy="8.3" r="4.2" fill="#000"/><circle cx="8.5" cy="8.3" r="2.2" fill="#fff"/></svg>
      <div>P O Box 00 .adress<br>and 00demoadress</div>
    </div>
  </header>

  <div class="card-under"></div>
  <section class="card card--front" aria-label="Visitenkarte Vorderseite">
    <div class="abs brand card-brand">QRTL Rechtsanwälte</div>
    <div class="abs person person__name">JONAS ACKERMANN</div>
    <div class="abs person person__role">lawyer</div>
    <div class="abs person person__field">Specialist lawyer for copyright and media law</div>
    <div class="abs divider"></div>
    <div class="abs divider__diamond"></div>

    <div class="abs contact contact--phone">
      <svg width="11" height="11" viewBox="0 0 11 11" aria-hidden="true"><circle cx="5.5" cy="5.5" r="5.5" fill="#6b6b6b"/><path d="M3.6 2.8l1 1-.5.8c.4.8 1 1.4 1.8 1.8l.8-.5 1 1-.6.9C5.2 7.6 3.4 5.8 3 3.4z" fill="#fff"/></svg>
      +49 711 483 15 260
    </div>
    <div class="abs contact contact--web">
      <svg width="11" height="11" viewBox="0 0 11 11" aria-hidden="true"><circle cx="5.5" cy="5.5" r="5.5" fill="#6b6b6b"/><rect x="2.8" y="3.6" width="5.4" height="3.8" fill="none" stroke="#fff" stroke-width=".8"/><path d="M2.8 3.6l2.7 2 2.7-2" fill="none" stroke="#fff" stroke-width=".8"/></svg>
      www.qrtl-recht.de
    </div>
    <div class="abs contact contact--mail">
      <svg width="11" height="11" viewBox="0 0 11 11" aria-hidden="true"><circle cx="5.5" cy="5.5" r="5.5" fill="#6b6b6b"/><circle cx="5.5" cy="5.5" r="3" fill="none" stroke="#fff" stroke-width=".7"/><path d="M2.5 5.5h6M5.5 2.5v6" stroke="#fff" stroke-width=".6"/></svg>
      ackermann@qrtl-recht.de
    </div>
    <svg class="abs contact-pin" width="12" height="15" viewBox="0 0 12 15" aria-hidden="true"><path d="M6 0C2.7 0 0 2.5 0 5.6 0 9.4 6 15 6 15s6-5.6 6-9.4C12 2.5 9.3 0 6 0z" fill="#6b6b6b"/><circle cx="6" cy="5.6" r="2.4" fill="#fff"/></svg>
    <div class="abs contact contact--address">Lindenweg 17, 70374 Stuttgart</div>
  </section>

  <section class="card card--back" aria-label="Visitenkarte Rückseite">
    <div class="abs skyline-brand">QRTL</div>
    <div class="abs tower-art" role="img" aria-label="Illustration: Berliner Fernsehturm und Stuttgarter Fernsehturm als Silhouette"></div>
    <div class="abs ground-line"></div>
    <div class="abs office">
      <div class="office__city">BERLIN</div>
      <div class="office__line">spreeufer 8b</div>
      <div class="office__line">10179 berlin</div>
      <div class="office__line">tel. +4930 742 18 650</div>
    </div>
  </section>

  <div class="abs brand brand--footer">QRTL</div>
  <div class="abs tower-art--footer" role="img" aria-label="Illustration: Fernsehtürme Berlin und Stuttgart als Silhouette"></div>
  <div class="abs footer-band"></div>
</main>
</body>
</html>
```